UK Online Auction Site needs a clever design

We need a contemporary landing page and registration page design for a UK auction website, that look equally at home on PC's and tablets . The design should be fresh, bright, clean, professional, robust, and familiar. We would like to see something clever but functional.

```html
<!DOCTYPE html>
<html lang="en">
<head>
<meta charset="utf-8">
<title>Lotmark – Online Auctions</title>
<link href="https://fonts.googleapis.com/css2?family=Roboto:wght@400;500;700&family=Roboto+Slab:wght@400;500&family=Open+Sans:wght@400;600&display=swap" rel="stylesheet">
<style>
:root{
  --blue:#2f72c2;
  --blue-dark:#1f5fa8;
  --link:#2a73c6;
  --red:#e8463a;
  --orange:#d84f2a;
  --sand:#f2c46d;
  --ink:#222;
  --muted:#666;
  --line:#d9d9d9;
  --footer:#2f343f;
  --footer-deep:#3a3f4a;
}
*{box-sizing:border-box;margin:0;padding:0}
html,body{width:900px;height:1200px;overflow:hidden;background:#fff;font-family:"Roboto",Arial,sans-serif;color:var(--ink)}
.page{position:relative;width:900px;height:1200px}
.abs{position:absolute}
.topbar{left:0;top:0;width:900px;height:18px;background:#000;color:#fff;font-size:8px;font-weight:500}
.topbar .nav{left:150px;top:4px}
.topbar .account{left:657px;top:4px;display:flex;gap:14px}
.topbar .account span{display:flex;align-items:center;gap:4px}
.header{left:0;top:18px;width:900px;height:54px;border-bottom:2px solid #e2e2e2}
.brand{left:150px;top:8px;display:flex;align-items:center;gap:8px;font-size:26px;font-weight:700;color:var(--blue)}
.brand i{display:block;width:18px;height:18px;border-radius:50%;background:var(--blue)}
.social{right:150px;top:18px;display:flex;gap:4px}
.social span{width:19px;height:19px;border-radius:3px;display:block}
.sidebar{left:150px;top:89px;width:136px;height:213px;border:1px solid var(--line);box-shadow:0 1px 2px rgba(0,0,0,.15)}
.sidebar h2{background:var(--blue);color:#fff;font-size:11px;font-weight:500;text-align:center;height:30px;line-height:30px}
.sidebar li{list-style:none;font-size:9px;height:22.2px;line-height:22px;padding-left:15px;border-bottom:1px solid #e3e3e3}
.sidebar li.active{background:#e8e8e8;border-left:3px solid var(--blue);padding-left:12px}
.search{left:302px;top:89px;width:448px;height:38px;background:var(--blue)}
.search .label{left:20px;top:12px;color:#fff;font-size:11px;font-weight:500}
.search .field{left:124px;top:5px;width:308px;height:28px;background:#fff;padding:3px}
.search .input{left:3px;top:3px;width:240px;height:22px;background:#fbe0d9;font-size:8px;color:#444;padding:6px 0 0 34px}
.search .btn{right:3px;top:5px;width:56px;height:18px;background:#1f8fd8;color:#fff;font-size:8px;font-weight:500;text-align:center;line-height:18px}
.banner{left:302px;top:134px;width:448px;height:168px;border:1px solid var(--line);padding:4px}
.banner .art{left:4px;top:4px;width:438px;height:158px;background:linear-gradient(90deg,var(--orange) 0 48%,var(--sand) 48%)}
.banner h3{left:20px;top:40px;font-family:"Roboto Slab",serif;font-weight:400;font-size:14px;line-height:19px;color:#fff}
.banner h3 b{font-weight:400;color:#f6d25a}
.banner p{left:20px;top:88px;width:160px;font-size:9.5px;color:#f2c3b4;line-height:13px}
.banner .buy{left:20px;top:122px;width:88px;height:24px;background:var(--blue-dark);color:#fff;font-size:10px;font-weight:700;text-align:center;line-height:24px}
.banner .off{left:198px;top:54px;width:50px;height:50px;border-radius:50%;background:#fff;border:2px solid var(--orange);color:var(--orange);font-size:9px;font-weight:700;text-align:center;padding-top:12px;line-height:10px}
.banner .photo{left:258px;top:18px;width:160px;height:124px;background:radial-gradient(circle at 50% 55%,#555,#1e1e1e 70%);border-radius:14px}
.info{left:150px;top:318px;width:600px;height:144px;border:1px solid var(--line)}
.col{top:0;height:142px;border-right:1px solid var(--line);padding:10px 5px}
.col h4{font-size:11px;font-weight:400;color:var(--link);margin-bottom:5px}
.col p{font-size:7px;line-height:14.5px;color:var(--muted)}
.welcome{left:0;width:131px}
.welcome ul{margin-top:3px}
.welcome li{list-style:none;font-size:7px;line-height:12.5px;color:#333;padding-left:11px;position:relative}
.welcome li:before{content:"";position:absolute;left:1px;top:3px;border-left:4px solid var(--blue);border-top:3px solid transparent;border-bottom:3px solid transparent}
.signin{left:131px;width:149px;padding-left:12px}
.signin .btn{margin-top:10px;width:110px;height:15px;background:var(--blue);color:#fff;font-size:8px;font-weight:500;text-align:center;line-height:15px;border-radius:2px}
.signin .reg{margin-top:9px;font-size:7px;color:var(--muted);padding-left:3px}
.signin .reg b{color:#222;font-weight:400}
.confidence{left:280px;width:158px;border-right:none;padding-left:19px}
.safe{display:flex;gap:8px;margin-top:5px;height:32px}
.safe svg{flex:none;margin-top:2px}
.safe strong{display:block;font-size:8px;font-weight:400;color:#222}
.safe span{display:block;font-size:6.5px;color:#666;line-height:9px}
.ad{left:438px;top:7px;width:155px;height:130px;background:linear-gradient(120deg,#4a5361,#1b1e24);}
.ad .tag{left:6px;top:24px;color:#fff;font-size:7px;line-height:8.5px}
.ad .strip{left:0;top:50px;width:155px;height:28px;background:rgba(47,114,194,.7);color:#fff;font-size:12px;padding:6px 0 0 66px}
.bar{left:150px;width:600px;height:37px;background:var(--blue);color:#fff;font-size:15px;padding:9px 10px}
.bar .arrows{right:0;top:0;display:flex;gap:2px}
.bar .arrows span{width:32px;height:37px;border-left:2px solid #fff;display:flex;align-items:center;justify-content:center}
.grid{left:150px;width:600px;height:192px}
.card{top:0;width:139px;height:192px;border:1px solid var(--line);box-shadow:0 1px 2px rgba(0,0,0,.12);background:#fff;overflow:hidden}
.card .sale{left:-14px;top:6px;width:50px;height:10px;background:var(--red);transform:rotate(-45deg);color:#fff;font-size:4.5px;text-align:center;line-height:10px;font-weight:700}
.card .pic{left:12px;top:12px;width:113px;height:98px;border-radius:4px}
.card .divider{left:0;top:122px;width:139px;height:1px;background:var(--line)}
.card .name{left:6px;top:132px;width:130px;font-size:7px;line-height:14.4px;color:var(--link)}
.card .row{left:0;top:163px;width:139px;height:28px;border-top:1px solid var(--line);display:flex}
.card .price{flex:1;font-size:7px;color:var(--red);padding:10px 0 0 16px;border-right:1px solid var(--line)}
.card .ico{width:31px;display:flex;align-items:center;justify-content:center;border-right:1px solid var(--line)}
.card .ico:last-child{border-right:none}
.card .quick{left:0;top:56px;width:139px;height:25px;background:rgba(120,170,225,.75);color:#fff;font-size:8px;display:flex;align-items:center;justify-content:center;gap:6px}
.newsletter{left:150px;top:1010px;width:600px;height:40px;background:#f6f6f6;border:1px solid #eee}
.newsletter .t{left:10px;top:11px;font-family:"Open Sans",sans-serif;font-size:14px;color:#333}
.newsletter .field{left:174px;top:10px;width:178px;height:20px;background:#fff;border:1px solid #ddd}
.newsletter .sub{left:356px;top:12px;width:54px;height:17px;background:var(--red);color:#fff;font-size:8px;font-weight:700;text-align:center;line-height:17px}
.newsletter .follow{left:430px;top:13px;font-family:"Open Sans",sans-serif;font-size:10px;color:#444}
.newsletter .rings{left:488px;top:6px;display:flex;gap:7px}
.newsletter .rings span{width:26px;height:26px;border-radius:50%;border:1.5px solid var(--red)}
.footer{left:0;top:1060px;width:900px;height:114px;background:var(--footer);border-top:4px solid var(--blue);color:#fff}
.fcol{top:19px}
.fcol h5{font-size:8.5px;font-weight:500;margin-bottom:9px}
.fcol li{list-style:none;font-size:7px;line-height:14.4px;color:#e5e5e5}
.contact li{display:flex;gap:9px;align-items:flex-start;margin-bottom:6px;line-height:9px}
.contact svg{flex:none}
.badge{left:806px;top:35px;font-size:8px;color:#fff}
.bottom{left:0;top:1174px;width:900px;height:26px;background:var(--footer-deep);color:#fff;font-size:7px}
.bottom .copy{left:150px;top:9px}
.bottom .lang{left:715px;top:6px;width:34px;height:15px;background:#fff;border:1px solid #ccc}
.bottom .lang i{position:absolute;left:3px;top:3px;width:14px;height:8px;background:#c33}
</style>
</head>
<body>
<div class="page">

  <div class="abs topbar">
    <div class="abs nav">Sell \ Sign In \ Basket \ Help \ Contact</div>
    <div class="abs account">
      <span><svg width="8" height="8" viewBox="0 0 8 8"><circle cx="4" cy="2.2" r="2" fill="#fff"/><path d="M0 8c0-3 8-3 8 0z" fill="#fff"/></svg>Register</span>
      <span><svg width="7" height="8" viewBox="0 0 7 8"><rect x="0" y="3.5" width="7" height="4.5" fill="#fff"/><path d="M1.5 3.5V2a2 2 0 0 1 4 0v1.5" stroke="#fff" fill="none"/></svg>Log In</span>
    </div>
  </div>

  <header class="abs header">
    <div class="abs brand"><i></i>Lotmark</div>
    <div class="abs social">
      <span style="background:#1da1f2"></span>
      <span style="background:#d8362b"></span>
      <span style="background:#3b5998"></span>
      <span style="background:#0e76a8"></span>
    </div>
  </header>

  <nav class="abs sidebar">
    <h2>Online stores</h2>
    <ul>
      <li>Computers</li>
      <li class="active">Fashion</li>
      <li>Electronics</li>
      <li>Apparels</li>
      <li>Cosmetics</li>
      <li>Furniture</li>
      <li>Toys &amp; Hobbies</li>
      <li style="border-bottom:none">Toys &amp; Hobbies</li>
    </ul>
  </nav>

  <div class="abs search">
    <div class="abs label">Search the Store</div>
    <div class="abs field">
      <div class="abs input">Ex. web design, frontend</div>
      <svg class="abs" style="left:14px;top:9px" width="11" height="11" viewBox="0 0 11 11"><circle cx="4.5" cy="4.5" r="3.5" stroke="#555" stroke-width="1.5" fill="none"/><path d="M7 7l3.5 3.5" stroke="#555" stroke-width="1.6"/></svg>
      <div class="abs btn">Search</div>
    </div>
  </div>

  <section class="abs banner">
    <div class="abs art"></div>
    <h3 class="abs"><b>Neque Porro Guisquam</b><br>Est Gui Dolorem</h3>
    <p class="abs">There are many variations of passages of Lorem</p>
    <div class="abs buy">BUY NOW</div>
    <div class="abs off">20%<br>OFF</div>
    <div class="abs photo" role="img" aria-label="Photo of a black digital SLR camera"></div>
  </section>

  <section class="abs info">
    <div class="abs col welcome">
      <h4>Welcome</h4>
      <p>Even if you're new or already experienced, we have everything you need to enjoy shopping on Lotmark.</p>
      <ul>
        <li>How do I pay for items?</li>
        <li>How do I leave feedback?</li>
        <li>How do I open a new store?</li>
        <li>How do I place bids?</li>
        <li>How do I ship my items?</li>
      </ul>
    </div>
    <div class="abs col signin">
      <h4>Sign In</h4>
      <p>Sign-in to your account in order to buy, sell or manage your preferences.</p>
      <div class="btn">Sign In</div>
      <div class="reg">Don't have an account? <b>Register ›</b></div>
    </div>
    <div class="abs col confidence">
      <h4>Shop with confidence</h4>
      <div class="safe">
        <svg width="18" height="20" viewBox="0 0 18 20"><path d="M9 0l9 3v6c0 6-4 9-9 11C4 18 0 15 0 9V3z" fill="#7a8a7a"/><path d="M4 10l3.5 3.5L14 6" stroke="#3fbf3f" stroke-width="2.5" fill="none"/></svg>
        <div><strong>Completely safe</strong><span>Bid on or buy items you're watching or searching for</span></div>
      </div>
      <div class="safe">
        <svg width="18" height="20" viewBox="0 0 18 20"><path d="M4 1h10v6a5 5 0 0 1-10 0z" fill="#e2a91e"/><rect x="8" y="12" width="2" height="4" fill="#c8901a"/><rect x="5" y="16" width="8" height="3" fill="#c8901a"/></svg>
        <div><strong>Completely safe</strong><span>Bid on or buy items you're watching or searching for</span></div>
      </div>
      <div class="safe">
        <svg width="18" height="20" viewBox="0 0 18 20"><rect x="0" y="3" width="18" height="7" rx="1" fill="#2f8fe0"/><circle cx="12" cy="14" r="3" fill="#fff" stroke="#555"/></svg>
        <div><strong>Completely safe</strong><span>Bid on or buy items you're watching or searching for</span></div>
      </div>
    </div>
    <div class="abs ad" role="img" aria-label="Advert photo of a digital SLR camera">
      <div class="abs tag">take<br>digital<br>to a pro<br>level</div>
      <div class="abs strip">Ads</div>
    </div>
  </section>

  <div class="abs bar" style="top:479px">Featured
    <div class="abs arrows">
      <span><svg width="5" height="6"><path d="M4 0v6L0 3z" fill="#fff"/></svg></span>
      <span><svg width="5" height="6"><path d="M1 0v6l4-3z" fill="#fff"/></svg></span>
    </div>
  </div>

  <div class="abs grid" style="top:530px">
    <article class="abs card" style="left:1px">
      <div class="abs pic" role="img" aria-label="Photo of a compact digital camera" style="background:#1f2a44"></div>
      <div class="abs sale">SALE</div>
      <div class="abs quick"><svg width="11" height="7" viewBox="0 0 11 7"><ellipse cx="5.5" cy="3.5" rx="5.5" ry="3.5" fill="#fff"/><circle cx="5.5" cy="3.5" r="1.6" fill="#1f2a44"/></svg>Quick View</div>
      <div class="abs divider"></div>
      <div class="abs name">Brevano Dream Versatile Red Espresso Coffee Machine</div>
      <div class="abs row"><div class="price">2.499,00 €</div>
        <div class="ico" style="background:var(--red)"><svg width="10" height="9" viewBox="0 0 10 9"><path d="M5 9L1 5a2.4 2.4 0 0 1 4-3 2.4 2.4 0 0 1 4 3z" fill="#fff"/></svg></div>
        <div class="ico" style="background:var(--blue)"><svg width="12" height="10" viewBox="0 0 12 10"><path d="M0 1h2l2 5h6l1.5-4H3" stroke="#fff" fill="none" stroke-width="1.2"/><circle cx="5" cy="8.5" r="1" fill="#fff"/><circle cx="9" cy="8.5" r="1" fill="#fff"/></svg></div>
      </div>
    </article>
    <article class="abs card" style="left:154px">
      <div class="abs pic" role="img" aria-label="Photo of a smartphone" style="background:linear-gradient(#fff,#e8eef6)"></div>
      <div class="abs sale">SALE</div>
      <div class="abs divider"></div>
      <div class="abs name">Brevano Dream Versatile Red Espresso Coffee Machine</div>
      <div class="abs row"><div class="price">1.899,00 €</div>
        <div class="ico"><svg width="10" height="9" viewBox="0 0 10 9"><path d="M5 9L1 5a2.4 2.4 0 0 1 4-3 2.4 2.4 0 0 1 4 3z" fill="var(--red)"/></svg></div>
        <div class="ico"><svg width="12" height="10" viewBox="0 0 12 10"><path d="M0 1h2l2 5h6l1.5-4H3" stroke="var(--blue)" fill="none" stroke-width="1.2"/><circle cx="5" cy="8.5" r="1" fill="var(--blue)"/><circle cx="9" cy="8.5" r="1" fill="var(--blue)"/></svg></div>
      </div>
    </article>
    <article class="abs card" style="left:304px">
      <div class="abs pic" role="img" aria-label="Photo of a desktop computer with keyboard" style="background:linear-gradient(#fff,#eef2f8)"></div>
      <div class="abs sale">SALE</div>
      <div class="abs divider"></div>
      <div class="abs name">Brevano Dream Versatile Red Espresso Coffee Machine</div>
      <div class="abs row"><div class="price">305,00 €</div>
        <div class="ico"><svg width="10" height="9" viewBox="0 0 10 9"><path d="M5 9L1 5a2.4 2.4 0 0 1 4-3 2.4 2.4 0 0 1 4 3z" fill="var(--red)"/></svg></div>
        <div class="ico"><svg width="12" height="10" viewBox="0 0 12 10"><path d="M0 1h2l2 5h6l1.5-4H3" stroke="var(--blue)" fill="none" stroke-width="1.2"/><circle cx="5" cy="8.5" r="1" fill="var(--blue)"/><circle cx="9" cy="8.5" r="1" fill="var(--blue)"/></svg></div>
      </div>
    </article>
    <article class="abs card" style="left:460px">
      <div class="abs pic" role="img" aria-label="Photo of a car GPS navigator on a mount" style="background:linear-gradient(#fff,#eceef1)"></div>
      <div class="abs sale">SALE</div>
      <div class="abs divider"></div>
      <div class="abs name">Brevano Dream Versatile Red Espresso Coffee Machine</div>
      <div class="abs row"><div class="price">2.499,00 €</div>
        <div class="ico"><svg width="10" height="9" viewBox="0 0 10 9"><path d="M5 9L1 5a2.4 2.4 0 0 1 4-3 2.4 2.4 0 0 1 4 3z" fill="var(--red)"/></svg></div>
        <div class="ico"><svg width="12" height="10" viewBox="0 0 12 10"><path d="M0 1h2l2 5h6l1.5-4H3" stroke="var(--blue)" fill="none" stroke-width="1.2"/><circle cx="5" cy="8.5" r="1" fill="var(--blue)"/><circle cx="9" cy="8.5" r="1" fill="var(--blue)"/></svg></div>
      </div>
    </article>
  </div>

  <div class="abs bar" style="top:750px">Items from seller stores
    <div class="abs arrows">
      <span><svg width="5" height="6"><path d="M4 0v6L0 3z" fill="#fff"/></svg></span>
      <span><svg width="5" height="6"><path d="M1 0v6l4-3z" fill="#fff"/></svg></span>
    </div>
  </div>

  <div class="abs grid" style="top:802px">
    <article class="abs card" style="left:1px">
      <div class="abs pic" role="img" aria-label="Photo of wired earphones" style="background:linear-gradient(#fff,#e9f6f4)"></div>
      <div class="abs sale">SALE</div>
      <div class="abs divider"></div>
      <div class="abs name">Brevano Dream Versatile Red Espresso Coffee Machine</div>
      <div class="abs row"><div class="price">2.499,00 €</div>
        <div class="ico"><svg width="10" height="9" viewBox="0 0 10 9"><path d="M5 9L1 5a2.4 2.4 0 0 1 4-3 2.4 2.4 0 0 1 4 3z" fill="var(--red)"/></svg></div>
        <div class="ico"><svg width="12" height="10" viewBox="0 0 12 10"><path d="M0 1h2l2 5h6l1.5-4H3" stroke="var(--blue)" fill="none" stroke-width="1.2"/><circle cx="5" cy="8.5" r="1" fill="var(--blue)"/><circle cx="9" cy="8.5" r="1" fill="var(--blue)"/></svg></div>
      </div>
    </article>
    <article class="abs card" style="left:154px">
      <div class="abs pic" role="img" aria-label="Photo of a tablet" style="background:linear-gradient(#fff,#eceff4)"></div>
      <div class="abs sale">SALE</div>
      <div class="abs divider"></div>
      <div class="abs name">Brevano Dream Versatile Red Espresso Coffee Machine</div>
      <div class="abs row"><div class="price">1.899,00 €</div>
        <div class="ico"><svg width="10" height="9" viewBox="0 0 10 9"><path d="M5 9L1 5a2.4 2.4 0 0 1 4-3 2.4 2.4 0 0 1 4 3z" fill="var(--red)"/></svg></div>
        <div class="ico"><svg width="12" height="10" viewBox="0 0 12 10"><path d="M0 1h2l2 5h6l1.5-4H3" stroke="var(--blue)" fill="none" stroke-width="1.2"/><circle cx="5" cy="8.5" r="1" fill="var(--blue)"/><circle cx="9" cy="8.5" r="1" fill="var(--blue)"/></svg></div>
      </div>
    </article>
    <article class="abs card" style="left:304px">
      <div class="abs pic" role="img" aria-label="Photo of a graphics card" style="background:linear-gradient(#fff,#ececec)"></div>
      <div class="abs sale">SALE</div>
      <div class="abs divider"></div>
      <div class="abs name">Brevano Dream Versatile Red Espresso Coffee Machine</div>
      <div class="abs row"><div class="price">305,00 €</div>
        <div class="ico"><svg width="10" height="9" viewBox="0 0 10 9"><path d="M5 9L1 5a2.4 2.4 0 0 1 4-3 2.4 2.4 0 0 1 4 3z" fill="var(--red)"/></svg></div>
        <div class="ico"><svg width="12" height="10" viewBox="0 0 12 10"><path d="M0 1h2l2 5h6l1.5-4H3" stroke="var(--blue)" fill="none" stroke-width="1.2"/><circle cx="5" cy="8.5" r="1" fill="var(--blue)"/><circle cx="9" cy="8.5" r="1" fill="var(--blue)"/></svg></div>
      </div>
    </article>
    <article class="abs card" style="left:460px">
      <div class="abs pic" role="img" aria-label="Photo of a black PC tower case" style="background:linear-gradient(#fff,#e6e6e6)"></div>
      <div class="abs sale">SALE</div>
      <div class="abs divider"></div>
      <div class="abs name">Brevano Dream Versatile Red Espresso Coffee Machine</div>
      <div class="abs row"><div class="price">2.499,00 €</div>
        <div class="ico"><svg width="10" height="9" viewBox="0 0 10 9"><path d="M5 9L1 5a2.4 2.4 0 0 1 4-3 2.4 2.4 0 0 1 4 3z" fill="var(--red)"/></svg></div>
        <div class="ico"><svg width="12" height="10" viewBox="0 0 12 10"><path d="M0 1h2l2 5h6l1.5-4H3" stroke="var(--blue)" fill="none" stroke-width="1.2"/><circle cx="5" cy="8.5" r="1" fill="var(--blue)"/><circle cx="9" cy="8.5" r="1" fill="var(--blue)"/></svg></div>
      </div>
    </article>
  </div>

  <section class="abs newsletter">
    <div class="abs t">Sign Up For Newsletter:</div>
    <div class="abs field"></div>
    <div class="abs sub">Subscribe</div>
    <div class="abs follow">Follow Me</div>
    <div class="abs rings"><span></span><span></span><span></span></div>
  </section>

  <footer class="abs footer">
    <div class="abs fcol" style="left:150px"><h5>Buy</h5><ul><li>Categories</li><li>Search</li><li>Currency Converter</li></ul></div>
    <div class="abs fcol" style="left:270px"><h5>Sell</h5><ul><li>Sell New Item</li><li>Sell Bulk Items</li></ul></div>
    <div class="abs fcol" style="left:385px"><h5>Support</h5><ul><li>Contact</li><li>Terms</li><li>Privacy</li><li>RSS</li></ul></div>
    <div class="abs fcol" style="left:505px"><h5>Other</h5><ul><li>About</li><li>News</li><li>Feeds</li></ul></div>
    <div class="abs fcol contact" style="left:638px"><h5>Contact</h5><ul>
      <li><svg width="7" height="9" viewBox="0 0 7 9"><path d="M3.5 9S0 5 0 3.5a3.5 3.5 0 0 1 7 0C7 5 3.5 9 3.5 9z" fill="#29b6f6"/><circle cx="3.5" cy="3.5" r="1.3" fill="var(--footer)"/></svg><span>14 Harbour Lane<br>Leeds, LS1 4AB</span></li>
      <li><svg width="7" height="9" viewBox="0 0 7 9"><rect x="0.5" y="0.5" width="6" height="8" rx="1" stroke="#29b6f6" fill="none"/></svg><span>0113 496 0127</span></li>
      <li><svg width="9" height="7" viewBox="0 0 9 7"><rect width="9" height="7" fill="#29b6f6"/><path d="M0 0l4.5 3.5L9 0" stroke="var(--footer)" fill="none"/></svg><span>Click here to email</span></li>
    </ul></div>
    <div class="abs badge">X18</div>
  </footer>

  <div class="abs bottom">
    <div class="abs copy">Copyright ©2014, Lotmark.</div>
    <div class="abs lang"><i></i></div>
  </div>

</div>
</body>
</html>
```